Need wine label for brand that is named: Casmerel Vineyards & Winery

Casmerel is a yoga way of breathing. In Sanskrit Casmerel means "flying up." I would like a creative wine label that articulates Casmerel. The label should include a graphic and the name Casmerel on one line and Vineyards & Winery in smaller print underneath Casmerel.

```html
<!DOCTYPE html>
<html lang="en">
<head>
<meta charset="utf-8">
<title>Casmerel Vineyards &amp; Winery – Wine Label</title>
<link rel="stylesheet" href="https://fonts.googleapis.com/css2?family=Tinos&family=Source+Sans+3:wght@400&display=swap">
<style>
  :root {
    --plum-deep: #8a3c8e;
    --plum-mid: #a257a8;
    --plum-light: #c48bc8;
    --plum-mist: #d9b2dc;
    --band-white: #ffffff;
    --band-blush: #cf98d0;
    --strip-grey-dark: #7d6f7e;
    --strip-grey-light: #c9bfca;
    --ink: #0d0d0d;
    --paper: #ffffff;
    --art-light: #f6eef7;
    --art-soft: #e4cbe6;
  }
  * { margin: 0; padding: 0; box-sizing: border-box; }
  html, body {
    width: 989px;
    height: 1200px;
    overflow: hidden;
    background: var(--plum-deep);
  }
  .wine-label {
    position: relative;
    width: 989px;
    height: 1200px;
    overflow: hidden;
    background:
      radial-gradient(ellipse at 85% 8%, var(--plum-mist) 0%, transparent 45%),
      radial-gradient(ellipse at 20% 30%, var(--plum-light) 0%, transparent 55%),
      linear-gradient(160deg, var(--plum-mid) 0%, var(--plum-deep) 70%, var(--plum-mid) 100%);
  }
  .grape-artwork {
    position: absolute;
    left: 308px;
    top: 67px;
    width: 532px;
    height: 597px;
  }
  .name-band {
    position: absolute;
    left: 0;
    top: 718px;
    width: 100%;
    height: 307px;
    background: linear-gradient(to bottom, var(--band-white) 0%, var(--band-white) 12%, var(--band-blush) 100%);
  }
  .brand-name {
    position: absolute;
    left: 0;
    top: 738px;
    width: 100%;
    text-align: center;
    font-family: "Tinos", "Times New Roman", serif;
    font-size: 206px;
    line-height: 1;
    color: var(--ink);
    letter-spacing: 1px;
  }
  .subtitle-strip {
    position: absolute;
    left: 0;
    top: 1025px;
    width: 100%;
    height: 99px;
    background: linear-gradient(to right, var(--strip-grey-dark) 0%, var(--strip-grey-light) 30%, var(--strip-grey-light) 70%, var(--strip-grey-dark) 100%);
  }
  .brand-subtitle {
    position: absolute;
    left: 0;
    top: 1034px;
    width: 100%;
    text-align: center;
    font-family: "Source Sans 3", "Helvetica Neue", sans-serif;
    font-size: 78px;
    line-height: 1;
    color: var(--paper);
    text-shadow: 0 1px 3px rgba(60, 40, 60, 0.45);
  }
  .base-band {
    position: absolute;
    left: 0;
    top: 1124px;
    width: 100%;
    height: 76px;
    background: linear-gradient(to right, var(--plum-mid), var(--plum-light), var(--plum-mid));
  }
</style>
</head>
<body>
  <main class="wine-label">
    <svg class="grape-artwork" role="img" aria-label="White illustration of a grape bunch with vine leaves and curling tendrils" viewBox="0 0 532 597" xmlns="http://www.w3.org/2000/svg">
      <defs>
        <radialGradient id="artGlow" cx="50%" cy="45%" r="60%">
          <stop offset="0%" stop-color="var(--art-light)" stop-opacity="0.95"/>
          <stop offset="100%" stop-color="var(--art-soft)" stop-opacity="0.35"/>
        </radialGradient>
      </defs>
      <rect width="532" height="597" rx="40" fill="url(#artGlow)"/>
    </svg>

    <div class="name-band"></div>
    <h1 class="brand-name">Casmerel</h1>

    <div class="subtitle-strip"></div>
    <p class="brand-subtitle">Vineyards &amp; Winery</p>

    <div class="base-band"></div>
  </main>
</body>
</html>
```